Astrological planner&diary book cover.

Book cover for print paperback. Title: "Whole Stargazer Journal & Logbook – Sign One (Sign Two, Sign Three etc) 2022: Shape your days by charting Orbital and Night angles and passages, Idle Drift, Night cycles, Sky almanac, and Reversing bodies." The book is a series of Astrological diary & planner for 2022 for each Zodiac sign (12 books in total). The design template should be the same – the only difference would be the Zodiac sign image and text.
It should be neutral to positive. There is no restriction regarding the colors – it can be both B&W and full color.
The design should be original and not include any images which require obtaining a copyright license to use. Symbols in common use and not copyrighted are probably ok.
Text for the back cover is not yet available, will be ready by the end of the project. I will need PDF, JPEG, TIFF (all formats both in CMYK and RGB), and the source file. For CMYK, we need files with no color profiles assigned.
I have several options in my mind (But please do not limit yourself by these options - please feel free to suggest your vision):
1) Is Gradient morning clear sky and the star constellation and image at skyrise (like a rising star)
2) solid dark color with image and symbols of the Zodiac sign
75% of my auditory are women

```html
<!DOCTYPE html>
<html lang="en">
<head>
<meta charset="utf-8">
<title>Whole Stargazer Journal &amp; Logbook 2022 – Cover</title>
<link rel="stylesheet" href="https://fonts.googleapis.com/css2?family=Cormorant+Garamond:wght@500;600&family=Uncial+Antiqua&family=Tinos&family=Cinzel:wght@500&display=swap">
<style>
  :root {
    --page-bg: #e6e4df;
    --sky-top: #1b1c5e;
    --sky-mid: #2a3aa8;
    --sky-glow: #3f8fe0;
    --horizon-pink: #f2b8d4;
    --horizon-cyan: #7fe0f2;
    --ground: #0b0d2a;
    --ink-light: #ffffff;
    --ink-soft: #eef2ff;
    --wheel-core: #dff4ff;
    --wheel-ring: #3aa6ea;
  }
  * { box-sizing: border-box; margin: 0; padding: 0; }
  html, body { width: 1200px; height: 1200px; overflow: hidden; }
  body { background: var(--page-bg); position: relative; }

  .cover {
    position: absolute;
    left: 230px; top: 30px;
    width: 740px; height: 1140px;
    background: linear-gradient(180deg, var(--sky-top) 0%, #23267a 35%, var(--sky-mid) 62%, var(--sky-glow) 82%, var(--horizon-cyan) 100%);
    overflow: hidden;
    box-shadow: 0 10px 30px rgba(0,0,0,.25);
    color: var(--ink-light);
  }

  .title-block { position: absolute; inset: 0; }
  .title-heading { font-weight: inherit; }
  .title-first, .title-main, .title-year, .title-kind, .title-signs {
    position: absolute; white-space: nowrap; display: block;
  }
  .title-first {
    left: 0; right: 0; top: 28px; text-align: center;
    font-family: "Cormorant Garamond", serif; font-weight: 600;
    font-size: 140px; line-height: 1; letter-spacing: 2px;
  }
  .title-main {
    left: 0; right: 0; top: 196px; text-align: center;
    font-family: "Cormorant Garamond", serif; font-weight: 600;
    font-size: 128px; line-height: 1; letter-spacing: 1px;
  }
  .title-year {
    right: 36px; top: 176px;
    font-family: "Cormorant Garamond", serif; font-weight: 500;
    font-size: 46px; line-height: 1;
  }
  .title-kind {
    left: 44px; top: 348px;
    font-family: "Uncial Antiqua", serif; font-size: 30px; line-height: 1;
  }
  .title-signs {
    right: 40px; top: 396px;
    font-family: "Uncial Antiqua", serif; font-size: 15px; line-height: 1;
    opacity: .95;
  }

  .divider { position: absolute; left: 110px; top: 424px; }

  .tagline {
    position: absolute; left: 50px; right: 50px; top: 474px;
    font-family: "Tinos", serif; font-size: 26px; line-height: 1.2;
    text-align: center; color: var(--ink-soft);
  }

  .wheel-art {
    position: absolute; left: 180px; top: 600px;
    width: 380px; height: 380px; border-radius: 50%;
    background: radial-gradient(circle, var(--wheel-core) 0%, #8fd2f6 14%, var(--wheel-ring) 30%, rgba(58,166,234,.35) 60%, rgba(42,58,168,0) 72%);
  }

  .horizon-art {
    position: absolute; left: 0; bottom: 0; width: 100%; height: 260px;
    background: linear-gradient(180deg, rgba(242,184,212,0) 0%, var(--horizon-pink) 45%, var(--ground) 78%, var(--ground) 100%);
  }

  .author {
    position: absolute; left: 0; right: 0; bottom: 60px;
    text-align: center; white-space: nowrap;
    font-family: "Cinzel", serif; font-weight: 500;
    font-size: 46px; letter-spacing: 2px; color: var(--ink-light);
  }
</style>
</head>
<body>
  <main class="cover">
    <header class="title-block">
      <h1 class="title-heading">
        <span class="title-first">Whole</span>
        <span class="title-year">2022</span>
        <span class="title-main">Stargazer</span>
      </h1>
      <span class="title-kind">journal &amp; logbook</span>
      <span class="title-signs">Sign One (Sign Two, Sign Three etc)</span>
      <svg class="divider" width="520" height="40" viewBox="0 0 520 40" aria-hidden="true">
        <line x1="10" y1="8" x2="250" y2="8" stroke="#fff" stroke-width="2"/>
        <line x1="270" y1="32" x2="510" y2="32" stroke="#fff" stroke-width="2"/>
        <circle cx="260" cy="20" r="6" fill="#fff"/>
      </svg>
    </header>

    <p class="tagline">Shape your days by charting Orbital and Night angles and passages, Idle Drift, Night cycles, Sky almanac, and Reversing bodies.</p>

    <div class="wheel-art" role="img" aria-label="Glowing zodiac wheel with sign symbols and constellations around a bright full moon"></div>

    <div class="horizon-art" role="img" aria-label="Pink and cyan dawn horizon over a dark hill with a figure raising both arms to the sky"></div>

    <p class="author">MAREN HOLLOWAY</p>
  </main>
</body>
</html>
```